New Signage for Cafe/Deli

We are looking to draw some attention to our café/deli at the end of a corridor in a commercial office building. The graphic panel should be 4'x8' with the name "Harborview Deli" somewhere in the middle. The deli mainly caters to the breakfast and lunch crowd. Attached are photos of the location (the exit sign will be moved)

Industry/Entity Type

Cafe

```html
<!DOCTYPE html>
<html lang="en">
<head>
<meta charset="utf-8">
<title>Harborview Deli – Corridor Signage</title>
<link rel="stylesheet" href="https://fonts.googleapis.com/css2?family=Black+Ops+One&family=Titan+One&family=Baloo+2:wght@700&family=Josefin+Sans:wght@400&display=swap">
<style>
  :root {
    --bg-deep: #1c1c12;
    --bg-olive: #34321d;
    --bg-warm: #6a4c22;
    --cream: #f4eeb2;
    --cream-light: #fbf3c8;
    --cream-dark: #e2cd86;
    --stitch: #b99f58;
    --menu-red: #6e1212;
    --accent-red: #ee2a3a;
    --white: #ffffff;
    --footer: #efe79c;
  }
  * { margin: 0; padding: 0; box-sizing: border-box; }
  html, body { width: 1200px; height: 2400px; overflow: hidden; background: var(--bg-deep); }

  .sign {
    position: relative;
    width: 1200px;
    height: 2400px;
    overflow: hidden;
    background:
      radial-gradient(ellipse 75% 40% at 50% 78%, var(--bg-warm) 0%, rgba(106,76,34,0.55) 45%, rgba(106,76,34,0) 100%),
      radial-gradient(ellipse 90% 60% at 50% 40%, var(--bg-olive) 0%, var(--bg-deep) 100%);
  }
  .sign::after {
    content: "";
    position: absolute;
    inset: 0;
    box-shadow: inset 0 0 220px 60px rgba(0,0,0,0.7);
    pointer-events: none;
  }

  .title {
    position: absolute;
    left: 0;
    top: 0;
    width: 1200px;
    height: 560px;
    font-weight: normal;
  }
  .title svg { display: block; width: 1200px; height: 560px; }
  .title__text {
    font-family: "Black Ops One", "Impact", sans-serif;
    fill: var(--cream);
    filter: drop-shadow(0 4px 8px rgba(0,0,0,0.45));
  }

  .beans {
    position: absolute;
    border-radius: 50%;
    background: radial-gradient(ellipse at center, rgba(244,238,178,0.22) 0%, rgba(244,238,178,0) 70%);
  }
  .beans--left { left: 40px; top: 440px; width: 400px; height: 240px; }
  .beans--right { left: 740px; top: 340px; width: 460px; height: 1040px; }

  .menu { position: absolute; left: 0; top: 600px; width: 1200px; height: 950px; }
  .menu__label {
    font-family: "Titan One", "Arial Black", sans-serif;
    fill: var(--menu-red);
    font-size: 76px;
  }

  .invite {
    position: absolute;
    left: 80px;
    top: 1555px;
    width: 1080px;
    font-family: "Baloo 2", "Arial Rounded MT Bold", sans-serif;
    font-weight: 700;
    font-size: 78px;
    line-height: 1.08;
    color: var(--white);
    transform: rotate(-3deg);
    transform-origin: left top;
  }
  .invite__highlight { color: var(--accent-red); }

  .cup {
    position: absolute;
    left: 340px;
    top: 1790px;
    width: 560px;
    height: 500px;
    border-radius: 50% 50% 46% 46% / 40% 40% 30% 30%;
    background: radial-gradient(ellipse at 45% 65%, #eadb92 0%, #c9b266 45%, rgba(140,110,50,0) 75%);
  }

  .footer {
    position: absolute;
    left: 0;
    bottom: 30px;
    width: 1200px;
    text-align: center;
    font-family: "Josefin Sans", "Helvetica", sans-serif;
    font-size: 42px;
    letter-spacing: 3px;
    color: var(--footer);
  }
</style>
</head>
<body>
<main class="sign">
  <h1 class="title">
    <svg viewBox="0 0 1200 560" aria-label="Harborview Deli">
      <text class="title__text" x="600" y="240" text-anchor="middle" font-size="180" textLength="1060" lengthAdjust="spacingAndGlyphs">HARBORVIEW</text>
      <text class="title__text" x="600" y="500" text-anchor="middle" font-size="300" textLength="560" lengthAdjust="spacingAndGlyphs">DELI</text>
    </svg>
  </h1>

  <div class="beans beans--left" role="img" aria-label="Scattered coffee beans"></div>
  <div class="beans beans--right" role="img" aria-label="Scattered coffee beans drifting up from the cup"></div>

  <svg class="menu" viewBox="0 0 1200 950" aria-label="Menu highlights">
    <defs>
      <linearGradient id="board-fill" x1="0" y1="0" x2="0" y2="1">
        <stop offset="0" stop-color="#fbf3c8"/>
        <stop offset="1" stop-color="#e2cd86"/>
      </linearGradient>
      <g id="board">
        <polygon points="-30,0 700,0 800,105 700,210 -30,210" fill="url(#board-fill)"/>
        <polygon points="-30,16 692,16 779,105 692,194 -30,194" fill="none" stroke="#b99f58" stroke-width="3" stroke-dasharray="12 8"/>
      </g>
    </defs>

    <g transform="translate(0,40) rotate(-4 400 105)">
      <use href="#board"/>
      <text class="menu__label" x="28" y="135" textLength="690" lengthAdjust="spacingAndGlyphs">ALL DAY BREAKFAST</text>
    </g>
    <g transform="translate(0,250) rotate(-4 400 105)">
      <use href="#board"/>
      <text class="menu__label" x="28" y="135" textLength="690" lengthAdjust="spacingAndGlyphs">BLT SANDWICHES</text>
    </g>
    <g transform="translate(0,462) rotate(-4 400 105)">
      <use href="#board"/>
      <text class="menu__label" x="120" y="135" textLength="455" lengthAdjust="spacingAndGlyphs">WESTERNS</text>
    </g>
    <g transform="translate(0,676) rotate(-4 400 105)">
      <use href="#board"/>
      <text class="menu__label" x="38" y="135" textLength="680" lengthAdjust="spacingAndGlyphs">GRILLED CHEESE</text>
    </g>
  </svg>

  <p class="invite">
    Join us for our daily <span class="invite__highlight">SPECIALS</span><br>
    and <span class="invite__highlight">HOME MADE SOUPS</span>
  </p>

  <div class="cup" role="img" aria-label="Illustration of a steaming coffee cup on a saucer"></div>

  <p class="footer">THE CAFE AT THE END OF THE CORRIDOR</p>
</main>
</body>
</html>
```